Breezeway Comfort business cards design

Need a business card design for a Heating and Air Conditioning business. I need these items included.
Business name: Breezeway Comfort
Owner: Marcus Tollefsen
License # 2874590
Phone number # 555-382-4071
Email: breezewaycomfortair@mailvista.example
Sales
Service
Installation
Maintenance

Heating and Air Conditioning

Requirements
Must have
• Company name , license number , phone number , email

```html
<!DOCTYPE html>
<html lang="en">
<head>
<meta charset="utf-8">
<title>Breezeway Comfort – Business Cards</title>
<link href="https://fonts.googleapis.com/css2?family=Orbitron:wght@600;700&family=Montserrat:wght@500;600;700&display=swap" rel="stylesheet">
<style>
  :root {
    --stage: #2b2b2e;
    --brand-blue: #2446b0;
    --brand-blue-deep: #1c3a98;
    --brand-orange: #f0642a;
    --sun-amber: #f6a13a;
    --ink: #1d1d1f;
    --paper: #ffffff;
  }
  * { margin: 0; padding: 0; box-sizing: border-box; }
  html, body { width: 1200px; height: 874px; overflow: hidden; }
  body {
    background: var(--stage);
    display: flex;
    flex-direction: column;
    align-items: center;
    justify-content: center;
    gap: 40px;
    font-family: "Montserrat", Arial, sans-serif;
  }
  .card {
    width: 640px;
    height: 366px;
    border-radius: 26px;
    position: relative;
    overflow: hidden;
  }

  /* Front */
  .card--front {
    background: radial-gradient(ellipse at 50% 45%, var(--brand-blue) 0%, var(--brand-blue-deep) 100%);
    color: var(--paper);
    display: flex;
    flex-direction: column;
    align-items: center;
    justify-content: center;
    gap: 44px;
  }
  .brand-mark {
    display: flex;
    align-items: center;
    gap: 18px;
  }
  .brand-mark__dot {
    width: 54px; height: 54px;
    border-radius: 50%;
    background: var(--brand-orange);
  }
  .brand-mark__name {
    font-family: "Orbitron", "Arial", sans-serif;
    font-weight: 700;
    font-size: 36px;
    letter-spacing: 1px;
    text-transform: uppercase;
    color: var(--paper);
  }
  .services {
    display: flex;
    align-items: center;
    gap: 10px;
    font-weight: 600;
    font-size: 17px;
  }
  .services__sep {
    width: 5px; height: 5px; border-radius: 50%;
    background: var(--brand-orange);
  }

  /* Back */
  .card--back {
    background: var(--paper);
    color: var(--ink);
  }
  .back-brand {
    position: absolute;
    left: 38px; top: 38px;
    font-family: "Orbitron", "Arial", sans-serif;
    font-weight: 700;
    font-size: 30px;
    text-transform: uppercase;
    color: var(--brand-blue);
    letter-spacing: 1px;
  }
  .owner {
    position: absolute;
    left: 44px; top: 138px;
  }
  .owner__name {
    font-family: "Orbitron", "Arial", sans-serif;
    font-weight: 600;
    font-size: 25px;
    color: var(--brand-blue);
  }
  .owner__role {
    font-size: 14px;
    font-weight: 500;
    margin-top: 2px;
  }
  .contact {
    position: absolute;
    left: 44px; top: 222px;
    list-style: none;
    display: flex;
    flex-direction: column;
    gap: 6px;
    font-size: 14.5px;
    font-weight: 500;
  }
  .contact__item { display: flex; align-items: center; gap: 9px; }
  .contact__icon { width: 13px; height: 13px; flex: none; }
  .license {
    position: absolute;
    left: 44px; top: 318px;
    font-weight: 700;
    font-size: 15px;
    color: var(--brand-orange);
  }
  .emblem-area {
    position: absolute;
    right: 44px; top: 112px;
    width: 210px; height: 210px;
    border-radius: 50%;
    background: linear-gradient(150deg, var(--sun-amber) 0%, var(--brand-orange) 50%, var(--brand-blue) 100%);
    opacity: 0.9;
  }
</style>
</head>
<body>

  <section class="card card--front" aria-label="Card front">
    <div class="brand-mark">
      <span class="brand-mark__dot"></span>
      <span class="brand-mark__name">Breezeway Comfort</span>
    </div>
    <p class="services">
      <span>Sales</span><span class="services__sep"></span>
      <span>Service</span><span class="services__sep"></span>
      <span>Installation</span><span class="services__sep"></span>
      <span>Maintenance</span>
    </p>
  </section>

  <section class="card card--back" aria-label="Card back">
    <h1 class="back-brand">Breezeway Comfort</h1>

    <div class="owner">
      <p class="owner__name">Marcus Tollefsen</p>
      <p class="owner__role">Owner</p>
    </div>

    <ul class="contact">
      <li class="contact__item">
        <svg class="contact__icon" viewBox="0 0 24 24" fill="var(--brand-orange)"><path d="M6.6 10.8a15.1 15.1 0 0 0 6.6 6.6l2.2-2.2c.3-.3.7-.4 1-.2 1.1.4 2.3.6 3.6.6.6 0 1 .4 1 1V20c0 .6-.4 1-1 1A17 17 0 0 1 3 4c0-.6.4-1 1-1h3.5c.6 0 1 .4 1 1 0 1.3.2 2.5.6 3.6.1.3 0 .7-.2 1z"/></svg>
        <span>555-382-4071</span>
      </li>
      <li class="contact__item">
        <svg class="contact__icon" viewBox="0 0 24 24" fill="var(--brand-orange)"><path d="M2 5h20v14H2z"/><path d="M2 5l10 8 10-8" fill="none" stroke="#fff" stroke-width="2"/></svg>
        <span>breezewaycomfortair@mailvista.example</span>
      </li>
      <li class="contact__item">
        <svg class="contact__icon" viewBox="0 0 24 24" fill="none" stroke="var(--brand-orange)" stroke-width="2.4"><circle cx="12" cy="12" r="9.5"/><path d="M2.5 12h19M12 2.5c3 3 3 16 0 19M12 2.5c-3 3-3 16 0 19"/></svg>
        <span>www.breezewaycomfortair.example</span>
      </li>
    </ul>

    <p class="license">License # 2874590</p>

    <div class="emblem-area" role="img" aria-label="Large brand emblem area in warm orange and cool blue tones"></div>
  </section>

</body>
</html>
```